RTM Global (Rooted Tillage and Meadowcraft) is a company positioning itself as a global leader in regenerative and sustainable agriculture and irrigation technologies and solutions, with a focus on soil health. Please read the attached information (which can be used in the website).
We're looking for a modern website which also compliments the agricultural sector and the natural resources we work with. We want the website to be fairly concise and to the point without elaborating too much. We would rather attract the clients to engage with us rather than drawing their own conclusions from the website.

```html
<!DOCTYPE html>
<html lang="en">
<head>
<meta charset="utf-8">
<title>RTM Global — Regenerative Agriculture</title>
<link rel="stylesheet" href="https://fonts.googleapis.com/css2?family=Roboto:wght@300;400;500;700;900&display=swap">
<style>
:root{
  --blue:#3f5f93;
  --blue-dark:#34507f;
  --sage:#8e9573;
  --sage-light:#9ea383;
  --tan:#c4b096;
  --gold:#c3a77e;
  --text:#333;
  --muted:#555;
  --white:#fff;
}
*{margin:0;padding:0;box-sizing:border-box}
html,body{width:1200px;height:3456px;overflow:hidden}
body{font-family:'Roboto',sans-serif;color:var(--text);background:var(--white);position:relative}
.abs{position:absolute}
.center{text-align:center;left:0;width:1200px}
.btn{position:absolute;display:flex;align-items:center;justify-content:center;border-radius:30px;font-weight:500;text-transform:uppercase;font-size:17px;letter-spacing:.2px}
.btn-sage{background:var(--sage);color:var(--white)}
.btn-white{background:var(--white);color:var(--blue)}
.rule{position:absolute;left:563px;width:74px;height:3px;background:var(--gold)}

/* header */
.topline{top:0;left:0;width:1200px;height:4px;background:var(--blue)}
.contact-pill{top:0;left:678px;width:409px;height:43px;background:var(--blue);border-radius:0 0 30px 30px;color:var(--white);font-size:13px;display:flex;align-items:center;justify-content:center;gap:14px}
.brand{top:44px;left:111px;display:flex;align-items:center;gap:10px}
.brand-dot{width:18px;height:18px;border-radius:50%;background:var(--blue)}
.brand-name{font-size:30px;font-weight:900;color:var(--blue);letter-spacing:-.5px}
.nav{top:80px;left:400px;display:flex;gap:22px;font-size:14px;font-weight:500;color:#222}
.nav .active{color:var(--gold);border-bottom:2px solid var(--gold);padding-bottom:2px}
.nav-cta{top:67px;left:940px;width:147px;height:43px;background:var(--white);color:var(--blue);box-shadow:0 3px 10px rgba(0,0,0,.15);font-size:15px}

/* hero */
.hero{top:134px;left:0;width:1200px;height:620px;background:linear-gradient(160deg,#6b4a2a 0%,#c6843b 35%,#e7a24a 55%,#8d5e33 80%,#4a3a2a 100%)}
.hero-curve{top:540px;left:0}
.hero-title{top:367px;color:var(--white);font-size:44px;line-height:50px;font-weight:700;text-transform:uppercase}
.hero-title span{display:block;font-weight:300}
.hero-rule{top:471px;background:var(--gold)}
.hero-sub{top:493px;color:var(--white);font-size:21px;line-height:29px}
.social{width:34px;height:34px;border:1.5px solid rgba(255,255,255,.8);border-radius:50%}
.social.on{background:var(--sage);border-color:var(--sage)}
.dot{width:11px;height:11px;border-radius:50%;background:rgba(255,255,255,.5)}

/* mission */
.h2{font-size:46px;text-transform:uppercase;color:var(--blue);letter-spacing:-.5px}
.h2 b{font-weight:900}
.h2 span{font-weight:300}
.mission-text{top:955px;left:131px;width:939px;text-align:center;font-size:18.5px;line-height:27.5px;color:#333}

/* products */
.products{top:1200px;left:0;width:1200px;height:822px}
.ring{left:111px;top:1509px;width:416px;height:416px;border-radius:50%;background:var(--white);box-shadow:0 0 20px rgba(0,0,0,.15)}
.ring-photo{left:159px;top:1537px;width:361px;height:361px;border-radius:50%;background:radial-gradient(circle at 50% 35%,#a9c6d6 0%,#6a8fa3 35%,#3f6b36 55%,#24421e 100%)}
.service-icon{width:82px;height:82px;border-radius:50%;background:var(--white);box-shadow:0 3px 10px rgba(0,0,0,.2);display:flex;align-items:center;justify-content:center}
.service-title{left:709px;width:380px;color:var(--white);font-size:20px;font-weight:500;text-transform:uppercase;line-height:26px}
.service-text{left:710px;width:377px;color:var(--white);font-size:13.5px;line-height:22.5px;text-align:justify}

/* why */
.card{top:2238px;width:302px;height:333px;background:var(--white);border-radius:26px;box-shadow:0 4px 16px rgba(0,0,0,.1);text-align:center}
.card-icon{margin:38px auto 0;width:102px;height:102px;border-radius:50%;border:3px dashed rgba(255,255,255,.7);outline:4px solid;display:flex;align-items:center;justify-content:center}
.card h3{margin-top:27px;font-size:17.5px;line-height:24px;color:var(--blue);font-weight:700;text-transform:uppercase}
.card p{margin:17px 22px 0;font-size:15px;line-height:24.5px;color:var(--muted)}

/* impact */
.impact{top:2683px;left:0;width:1200px;height:420px;background:linear-gradient(180deg,#959a78,#a3a78b)}
.impact-text{top:2829px;left:130px;width:940px;text-align:center;color:var(--white);font-size:18px;line-height:27.5px}

/* footer */
.footer-col h4{font-size:18px;font-weight:500;color:var(--white);text-transform:uppercase;margin-bottom:19px}
.footer-col li{list-style:none;color:var(--white);font-size:14px;height:43px;display:flex;align-items:flex-start;gap:19px}
.bullet{width:13px;height:13px;border-radius:50%;background:rgba(255,255,255,.35);margin-top:2px}
.c-icon{width:36px;height:36px;border-radius:50%;background:var(--white);display:flex;align-items:center;justify-content:center}
.c-label{color:var(--white);font-size:14.5px;font-weight:500}
.c-val{color:var(--white);font-size:12px;line-height:20px;margin-top:4px}
.f-social{width:34px;height:34px;border-radius:50%;border:1.5px solid rgba(255,255,255,.6)}
</style>
</head>
<body>

<!-- header -->
<div class="abs topline"></div>
<div class="abs contact-pill">
  <svg width="12" height="12" viewBox="0 0 24 24"><path fill="#fff" d="M6.6 10.8a15 15 0 0 0 6.6 6.6l2.2-2.2c.3-.3.7-.4 1-.2 1.1.4 2.3.6 3.6.6.6 0 1 .4 1 1V20c0 .6-.4 1-1 1A17 17 0 0 1 3 4c0-.6.4-1 1-1h3.5c.6 0 1 .4 1 1 0 1.3.2 2.5.6 3.6.1.3 0 .7-.2 1z"/></svg>
  <span>+1 (888) 888 8888</span><span>|</span>
  <svg width="13" height="11" viewBox="0 0 24 18"><path fill="#fff" d="M0 0h24v18H0z"/><path fill="none" stroke="#3f5f93" stroke-width="2" d="M1 1l11 9 11-9"/></svg>
  <span>info@rtmglobal.com</span>
</div>
<div class="abs brand"><div class="brand-dot"></div><div class="brand-name">RTM Global</div></div>
<nav class="abs nav">
  <span class="active">HOME</span><span>ABOUT US</span><span>WHY CHOOSE RTM?</span><span>PRODUCTS AND SERVICES</span>
</nav>
<div class="btn nav-cta">Contact Us</div>

<!-- hero -->
<div class="abs hero" role="img" aria-label="Smiling farmer holding a tablet in a field at sunset"></div>
<svg class="abs hero-curve" width="1200" height="220" viewBox="0 0 1200 220">
  <path d="M0 45 Q600 340 1200 40 L1200 0 Q600 260 0 45Z" fill="#8e9573"/>
  <path d="M0 45 Q600 260 1200 0 L1200 220 L0 220Z" fill="none"/>
  <path d="M0 40 L0 220 L1200 220 L1200 40 Q600 350 0 40Z" fill="#fff"/>
  <path d="M0 40 Q600 350 1200 40" fill="none" stroke="#8e9573" stroke-width="0"/>
</svg>
<div class="abs center hero-title">Revolutionizing Agriculture with<span>Regenerative Solutions</span></div>
<div class="rule hero-rule" style="top:471px"></div>
<div class="abs center hero-sub">Mobile Drip Irrigation | Agronomy | Soil Health |<br>Regenerative Technologies</div>
<div class="btn btn-sage" style="left:526px;top:573px;width:148px;height:42px;font-size:15px">Contact Us</div>
<div class="abs dot" style="left:583px;top:697px;background:#fff"></div>
<div class="abs dot" style="left:606px;top:697px"></div>
<div class="abs dot" style="left:629px;top:697px"></div>
<div class="abs social" style="left:1126px;top:313px"></div>
<div class="abs social on" style="left:1126px;top:356px"></div>
<div class="abs social" style="left:1126px;top:399px"></div>

<!-- mission -->
<h2 class="abs center h2" style="top:868px"><b>Our</b> <span>Mission</span></h2>
<div class="rule" style="top:922px"></div>
<p class="abs mission-text">At RTM, we are committed to reshaping the future of farming through regenerative agriculture. Our solutions go beyond sustainability, actively restoring ecosystems and improving soil health while delivering superior yields. With water-efficient irrigation, innovative agronomy, and a deep focus on soil vitality, we empower farmers to grow more sustainably and profitably.</p>
<div class="btn btn-sage" style="left:520px;top:1094px;width:160px;height:49px">Learn More</div>

<!-- products -->
<svg class="abs products" width="1200" height="822" viewBox="0 0 1200 822" role="img" aria-label="Tractor in a field under a tan overlay">
  <defs><linearGradient id="tan" x1="0" y1="0" x2="1" y2="1"><stop offset="0" stop-color="#c9b79e"/><stop offset="1" stop-color="#b9a385"/></linearGradient></defs>
  <path d="M0 25 Q70 -5 150 20 T300 35 T440 30 T560 75 T700 30 T820 10 T960 35 T1100 20 T1200 10 L1200 822 L0 822Z" fill="url(#tan)"/>
</svg>
<h2 class="abs center" style="top:1333px;color:#fff;font-size:45px;line-height:51px;text-transform:uppercase"><b style="font-weight:900">Our Core Products</b><br><span style="font-weight:300">and Services</span></h2>
<div class="abs ring"></div>
<div class="abs ring-photo" role="img" aria-label="Red tractor working a green crop field with digital overlay"></div>

<div class="abs service-icon" style="left:598px;top:1499px"><svg width="40" height="40" viewBox="0 0 40 40"><circle cx="20" cy="20" r="11" fill="none" stroke="#8e9573" stroke-width="4" stroke-dasharray="5 3"/><circle cx="20" cy="20" r="4" fill="#8e9573"/></svg></div>
<div class="abs service-title" style="top:1474px">Regenerative Agricultural Technologies</div>
<p class="abs service-text" style="top:1532px">Unlock the future of farming with the latest practices and tools designed to rebuild ecosystems, improve biodiversity, and restore soil carbon levels.</p>

<div class="abs service-icon" style="left:598px;top:1620px"><svg width="40" height="40" viewBox="0 0 40 40"><path d="M20 8c-4 6-6 9-6 12a6 6 0 0 0 12 0c0-3-2-6-6-12z" fill="#8e9573"/><path d="M8 30c4-4 8-4 12 0 4-4 8-4 12 0" fill="none" stroke="#8e9573" stroke-width="3"/></svg></div>
<div class="abs service-title" style="top:1622px">Mobile Drip Irrigation (MDI)</div>
<p class="abs service-text" style="top:1656px">Our advanced irrigation system maximizes water use efficiency, reduces waste, and promotes healthier crops.</p>

<div class="abs service-icon" style="left:598px;top:1741px"><svg width="40" height="40" viewBox="0 0 40 40"><circle cx="20" cy="20" r="12" fill="none" stroke="#8e9573" stroke-width="5" stroke-dasharray="4 3"/><circle cx="20" cy="20" r="5" fill="none" stroke="#8e9573" stroke-width="3"/></svg></div>
<div class="abs service-title" style="top:1743px">Agronomy Services</div>
<p class="abs service-text" style="top:1777px">Expert advice and customized crop management plans to boost productivity while supporting regenerative outcomes.</p>

<div class="abs service-icon" style="left:598px;top:1867px"><svg width="40" height="40" viewBox="0 0 40 40"><path d="M20 34V14M20 20c-6 0-9-4-9-8 5 0 9 3 9 8zm0 0c6 0 9-4 9-8-5 0-9 3-9 8z" fill="none" stroke="#8e9573" stroke-width="3"/><path d="M8 34h24" stroke="#8e9573" stroke-width="3"/></svg></div>
<div class="abs service-title" style="top:1856px">Soil Health Solutions</div>
<p class="abs service-text" style="top:1890px">From analysis to rehabilitation, we help you restore soil fertility, improve water retention, and reduce dependency on chemical inputs.</p>

<!-- why choose -->
<h2 class="abs center h2" style="top:2133px"><b>Why Choose</b> <span>RTM?</span></h2>
<div class="rule" style="top:2187px"></div>
<svg class="abs" style="left:38px;top:2392px" width="38" height="24" viewBox="0 0 38 24"><path d="M37 12H2M12 2L2 12l10 10" fill="none" stroke="#666" stroke-width="2"/></svg>
<svg class="abs" style="left:1124px;top:2392px" width="38" height="24" viewBox="0 0 38 24"><path d="M1 12h35M26 2l10 10-10 10" fill="none" stroke="#666" stroke-width="2"/></svg>

<div class="abs card" style="left:111px">
  <div class="card-icon" style="background:var(--sage);outline-color:var(--sage)"><svg width="44" height="44" viewBox="0 0 44 44"><path d="M22 40V12M14 40V18M30 40V18" stroke="#fff" stroke-width="3"/><path d="M8 30h28" stroke="#fff" stroke-width="3"/></svg></div>
  <h3>Champions of<br>Regenerative Agriculture</h3>
  <p>We don't just sustain—we regenerate, creating long-term benefits for the environment and your farm.</p>
</div>
<div class="abs card" style="left:448px">
  <div class="card-icon" style="background:var(--gold);outline-color:var(--gold)"><svg width="44" height="44" viewBox="0 0 44 44"><path d="M36 8c-10 0-18 8-22 18l4 4c10-4 18-12 18-22z" fill="#fff"/><path d="M12 28l-5 9 9-5" fill="#fff"/></svg></div>
  <h3>Cutting-Edge<br>Innovation</h3>
  <p>Access the latest technologies that promote ecosystem restoration and climate resilience.</p>
</div>
<div class="abs card" style="left:785px">
  <div class="card-icon" style="background:var(--sage);outline-color:var(--sage)"><svg width="44" height="44" viewBox="0 0 44 44"><circle cx="22" cy="16" r="6" fill="#fff"/><path d="M10 20c0 10 5 16 12 16s12-6 12-16" fill="none" stroke="#fff" stroke-width="4"/></svg></div>
  <h3>Tailored for Your<br>Success</h3>
  <p>We work with you to create strategies that meet the unique needs of your farm and community.</p>
</div>

<!-- impact -->
<div class="abs impact" role="img" aria-label="Faded field with network lines under a sage overlay"></div>
<h2 class="abs center" style="top:2745px;color:#fff;font-size:45px;text-transform:uppercase"><b style="font-weight:900">Our</b> <span style="font-weight:300">Impact</span></h2>
<div class="rule" style="top:2798px;background:#fff"></div>
<p class="abs impact-text">We are proud to help farmers build resilient farms, sequester carbon, and regenerate the land. Our approach ensures healthy soils, vibrant ecosystems, and productive crops for generations to come.</p>
<div class="btn btn-white" style="left:519px;top:2907px;width:160px;height:49px">Learn More</div>

<!-- footer -->
<svg class="abs" style="left:0;top:3010px" width="1200" height="446" viewBox="0 0 1200 446">
  <path d="M0 180 Q600 -160 1200 180 L1200 446 L0 446Z" fill="#fff"/>
  <path d="M0 198 Q600 -120 1200 198 L1200 446 L0 446Z" fill="#44649a"/>
</svg>
<div class="abs" style="left:111px;top:3225px;width:210px;text-align:center;color:#fff">
  <div style="width:16px;height:16px;border-radius:50%;background:#fff;margin:0 auto 10px"></div>
  <div style="font-size:34px;font-weight:900;letter-spacing:-.5px">RTM Global</div>
  <div style="font-size:10.5px;margin-top:6px">Rooted Tillage and Meadowcraft</div>
</div>

<div class="abs footer-col" style="left:370px;top:3122px">
  <h4>Navigation</h4>
  <ul>
    <li><span class="bullet"></span>Home</li>
    <li><span class="bullet"></span>About Us</li>
    <li><span class="bullet"></span>Why Choose RTM?</li>
    <li><span class="bullet"></span>Products and Services</li>
    <li><span class="bullet"></span>Contact Us</li>
  </ul>
</div>
<div class="abs footer-col" style="left:610px;top:3122px">
  <h4>Quick Links</h4>
  <ul>
    <li><span class="bullet"></span>Site Map</li>
    <li><span class="bullet"></span>Disclaimer</li>
    <li><span class="bullet"></span>Privacy Policy</li>
    <li><span class="bullet"></span>Terms &amp; Conditions</li>
  </ul>
</div>
<div class="abs footer-col" style="left:832px;top:3122px"><h4>Contact Us</h4></div>

<div class="abs c-icon" style="left:833px;top:3174px"><svg width="14" height="18" viewBox="0 0 14 18"><path d="M7 0a7 7 0 0 0-7 7c0 5 7 11 7 11s7-6 7-11a7 7 0 0 0-7-7z" fill="#44649a"/><circle cx="7" cy="7" r="2.5" fill="#fff"/></svg></div>
<div class="abs" style="left:891px;top:3181px;width:200px"><div class="c-label">LOCATIONS:</div><div class="c-val">465, Lorum Ipsum Dolore Sed Ameat, United States</div></div>
<div class="abs c-icon" style="left:833px;top:3253px"><svg width="16" height="16" viewBox="0 0 24 24"><path fill="#44649a" d="M6.6 10.8a15 15 0 0 0 6.6 6.6l2.2-2.2c.3-.3.7-.4 1-.2 1.1.4 2.3.6 3.6.6.6 0 1 .4 1 1V20c0 .6-.4 1-1 1A17 17 0 0 1 3 4c0-.6.4-1 1-1h3.5c.6 0 1 .4 1 1 0 1.3.2 2.5.6 3.6.1.3 0 .7-.2 1z"/></svg></div>
<div class="abs" style="left:891px;top:3260px"><div class="c-label">PHONE:</div><div class="c-val">+1 (888) 888 8888</div></div>
<div class="abs c-icon" style="left:833px;top:3315px"><svg width="16" height="12" viewBox="0 0 24 18"><path fill="#44649a" d="M0 0h24v18H0z"/><path fill="none" stroke="#fff" stroke-width="2" d="M1 1l11 9 11-9"/></svg></div>
<div class="abs" style="left:891px;top:3322px"><div class="c-label">EMAIL:</div><div class="c-val">info@rtmglobal.com</div></div>

<div class="abs" style="left:111px;top:3392px;width:976px;height:1px;background:rgba(255,255,255,.3)"></div>
<div class="abs" style="left:0;width:1000px;top:3414px;text-align:center;color:#fff;font-size:12.5px">© 2024 RTM GLOBAL &nbsp;|&nbsp; All Rights Reserved</div>
<div class="abs f-social" style="left:973px;top:3404px"></div>
<div class="abs f-social" style="left:1013px;top:3404px;background:var(--sage);border-color:var(--sage)"></div>
<div class="abs f-social" style="left:1054px;top:3404px"></div>

</body>
</html>
```